Birchline Septic Solutions

Would like to see some single sided ones but would also like to see some double sided with one sided only being the logo. Owners name is Tom Waldrick. Phone number is 555-214-8830
Services are pumping, inspections, installs, and repairs

Contact Information for Business Card

555-241-8830 Tom Waldrick Maple Ridge, OH

```html
<!DOCTYPE html>
<html lang="en">
<head>
<meta charset="utf-8">
<title>Birchline Septic Solutions – Business Card</title>
<link rel="stylesheet" href="https://fonts.googleapis.com/css2?family=Montserrat:wght@400;500;700;800&display=swap">
<style>
  :root {
    --backdrop: #26292d;
    --card-white: #ffffff;
    --band-black: #1e1e1f;
    --accent-teal: #2bb3b1;
    --text-light: #f2f2f2;
    --ink: #1a1a1a;
  }
  html, body {
    margin: 0;
    width: 1200px;
    height: 900px;
    overflow: hidden;
    background: var(--backdrop);
    font-family: "Montserrat", sans-serif;
  }
  .canvas {
    position: relative;
    width: 1200px;
    height: 900px;
  }
  .business-card {
    position: absolute;
    left: 100px;
    top: 164px;
    width: 1000px;
    height: 572px;
    border-radius: 36px;
    overflow: hidden;
    background: var(--card-white);
    box-shadow: 0 20px 50px rgba(0,0,0,0.45);
  }
  .card-art {
    position: absolute;
    inset: 0;
    width: 100%;
    height: 100%;
  }
  .band { fill: var(--band-black); }
  .stripe-teal { fill: var(--accent-teal); }
  .contact-block {
    position: absolute;
    left: 80px;
    top: 150px;
    color: var(--text-light);
  }
  .owner-name {
    margin: 0;
    font-size: 38px;
    font-weight: 700;
    letter-spacing: 0.5px;
    color: var(--accent-teal);
    text-transform: uppercase;
    line-height: 1;
    white-space: nowrap;
  }
  .owner-city {
    margin: 14px 0 0;
    font-size: 24px;
    font-weight: 500;
    line-height: 1;
    white-space: nowrap;
  }
  .divider {
    position: absolute;
    left: 300px;
    top: 240px;
    width: 2px;
    height: 110px;
    background: var(--accent-teal);
    opacity: 0.8;
  }
  .phone {
    position: absolute;
    left: 326px;
    top: 300px;
    display: flex;
    align-items: center;
    gap: 12px;
    font-size: 32px;
    font-weight: 500;
    color: var(--text-light);
    letter-spacing: 1px;
    line-height: 1;
    white-space: nowrap;
  }
  .phone-icon { width: 24px; height: 24px; fill: var(--accent-teal); }
  .brand {
    position: absolute;
    left: 620px;
    top: 150px;
    width: 340px;
    text-align: center;
    color: var(--ink);
    font-weight: 800;
    text-transform: uppercase;
  }
  .brand-name {
    margin: 0;
    font-size: 46px;
    letter-spacing: 2px;
    line-height: 1;
  }
  .brand-tagline {
    margin: 14px 0 0;
    font-size: 18px;
    letter-spacing: 5px;
    line-height: 1;
  }
</style>
</head>
<body>
<main class="canvas">
  <section class="business-card" aria-label="Birchline Septic Solutions business card">
    <svg class="card-art" viewBox="0 0 1000 572" preserveAspectRatio="none" aria-hidden="true">
      <path class="band" d="M40,0 H95 C330,20 470,70 560,140 C460,85 300,35 40,0 Z"/>
      <path class="stripe-teal" d="M470,170 C640,260 760,400 820,572 H796 C740,410 630,280 470,170 Z"/>
      <path class="band" d="M0,0 H150 C470,50 700,260 780,572 H0 Z"/>
    </svg>

    <div class="contact-block">
      <h1 class="owner-name">Tom Waldrick</h1>
      <p class="owner-city">Maple Ridge, OH</p>
    </div>
    <div class="divider"></div>
    <div class="phone">
      <svg class="phone-icon" viewBox="0 0 24 24" aria-hidden="true">
        <path d="M6.6 10.8c1.4 2.8 3.8 5.1 6.6 6.6l2.2-2.2c.3-.3.7-.4 1-.2 1.1.4 2.3.6 3.6.6.6 0 1 .4 1 1V20c0 .6-.4 1-1 1C10.6 21 3 13.4 3 4c0-.6.4-1 1-1h3.5c.6 0 1 .4 1 1 0 1.3.2 2.5.6 3.6.1.3 0 .7-.2 1L6.6 10.8z"/>
      </svg>
      <span class="phone-number">555-241-8830</span>
    </div>

    <div class="brand">
      <p class="brand-name">Birchline</p>
      <p class="brand-tagline">Septic Solutions</p>
    </div>
  </section>
</main>
</body>
</html>
```